I am about to have my Grandma's memoir printed. I am planning to go with an image wrap soft cover. The book is B5 page size 6.9" X 9.8" I am looking for help to make the cover for this special project stand out in a good way. I have included some photos that could be used but it's not necessary to use all of them, they are only provided to give an idea about the tone of the book being a picture of her whole life from being raised on a homestead, to living all the way through the modern era.

Requirements
Must have
• A feel that supports the title of the book "Ferryman's Promise"

```html
<!DOCTYPE html>
<html lang="en">
<head>
<meta charset="utf-8">
<title>Ferryman's Promise – A Memoir</title>
<link rel="stylesheet" href="https://fonts.googleapis.com/css2?family=Saira+Condensed:wght@400&family=Open+Sans:wght@300&display=swap">
<style>
  :root {
    --cover-black: #0b0b0b;
    --facet-dark: #1a1b1c;
    --facet-mid: #202122;
    --facet-edge: #080808;
    --frame-silver: #b9b6b4;
    --title-white: #ffffff;
    --subtitle-grey: #d8d8d8;
  }
  html, body {
    margin: 0;
    padding: 0;
    width: 845px;
    height: 1200px;
    overflow: hidden;
    background: var(--cover-black);
  }
  .cover {
    position: relative;
    width: 845px;
    height: 1200px;
    background: var(--cover-black);
    overflow: hidden;
  }
  .facets {
    position: absolute;
    left: 0;
    top: 0;
    width: 845px;
    height: 1200px;
  }
  .cover-title {
    position: absolute;
    top: 62px;
    left: 0;
    width: 100%;
    margin: 0;
    text-align: center;
    font-family: "Saira Condensed", "Arial Narrow", sans-serif;
    font-weight: 400;
    font-size: 80px;
    line-height: 1;
    letter-spacing: 3px;
    color: var(--title-white);
  }
  .cover-subtitle {
    position: absolute;
    top: 164px;
    left: 0;
    width: 100%;
    margin: 0;
    text-align: center;
    font-family: "Open Sans", Arial, sans-serif;
    font-weight: 300;
    font-size: 42px;
    line-height: 1;
    letter-spacing: -0.5px;
    color: var(--subtitle-grey);
  }
  .facet-bg { fill: var(--facet-dark); stroke: var(--facet-edge); stroke-width: 10; }
  .facet-bg-mid { fill: var(--facet-mid); stroke: var(--facet-edge); stroke-width: 10; }
  .photo-frame { stroke: var(--frame-silver); stroke-width: 4; stroke-linejoin: miter; }
</style>
</head>
<body>
<main class="cover">
  <svg class="facets" viewBox="0 0 1056 1500" preserveAspectRatio="none" xmlns="http://www.w3.org/2000/svg">
    <defs>
      <linearGradient id="portrait-tones" x1="0" y1="0" x2="0" y2="1">
        <stop offset="0" stop-color="#6d8a8a"/>
        <stop offset="0.25" stop-color="#5a3620"/>
        <stop offset="0.45" stop-color="#c99a84"/>
        <stop offset="0.65" stop-color="#e6dfd2"/>
        <stop offset="1" stop-color="#3f7a34"/>
      </linearGradient>
      <linearGradient id="ranch-tones" gradientUnits="userSpaceOnUse" x1="0" y1="800" x2="0" y2="1500">
        <stop offset="0" stop-color="#2e2e2e"/>
        <stop offset="0.35" stop-color="#5a5a5a"/>
        <stop offset="0.6" stop-color="#9d9d9d"/>
        <stop offset="1" stop-color="#c4c4c4"/>
      </linearGradient>
    </defs>

    <g class="background-facets">
      <polygon class="facet-bg" points="0,560 330,800 0,960"/>
      <polygon class="facet-bg-mid" points="45,640 300,790 45,950"/>
      <polygon class="facet-bg" points="200,700 355,615 355,790"/>
      <polygon class="facet-bg" points="740,560 1056,470 1056,690"/>
      <polygon class="facet-bg-mid" points="740,720 1056,610 1056,860"/>
      <polygon class="facet-bg" points="900,615 1056,540 1056,700"/>
      <polygon class="facet-bg" points="660,790 880,880 660,980"/>
      <polygon class="facet-bg-mid" points="950,780 1056,720 1056,880"/>
    </g>

    <g role="img" aria-label="Colour portrait photograph of the author smiling in a floral blouse">
      <polygon class="photo-frame" fill="url(#portrait-tones)" points="383,316 383,895 870,640"/>
    </g>

    <g role="img" aria-label="Black and white photograph of the author as a young woman on a white horse beside a vintage car">
      <polygon class="photo-frame" fill="url(#ranch-tones)" points="157,823 157,1330 630,1075"/>
      <polygon class="photo-frame" fill="url(#ranch-tones)" points="405,915 657,790 657,1068"/>
      <polygon class="photo-frame" fill="url(#ranch-tones)" points="682,890 682,1055 830,970"/>
      <polygon class="photo-frame" fill="url(#ranch-tones)" points="490,1185 1056,885 1056,1450"/>
      <polygon class="photo-frame" fill="url(#ranch-tones)" points="0,1000 125,1060 0,1125"/>
      <polygon class="photo-frame" fill="url(#ranch-tones)" points="0,1160 135,1095 135,1370"/>
      <polygon class="photo-frame" fill="url(#ranch-tones)" points="140,1385 490,1195 490,1500"/>
      <polygon class="photo-frame" fill="url(#ranch-tones)" points="0,1390 140,1460 0,1500"/>
      <polygon class="photo-frame" fill="url(#ranch-tones)" points="500,1220 720,1360 500,1500"/>
      <polygon class="photo-frame" fill="url(#ranch-tones)" points="600,1500 750,1385 750,1500"/>
      <polygon class="photo-frame" fill="url(#ranch-tones)" points="780,1385 1056,1460 780,1500"/>
    </g>
  </svg>

  <h1 class="cover-title">Ferryman's Promise</h1>
  <p class="cover-subtitle">A Memoir</p>
</main>
</body>
</html>
```